Cedarline Coalition Web Presence Design and Relaunch

Take existing web files and "clean up" for a a more presentable web landing pad.
posted presently on a site pad CSS template. at www.cedarlinecoalition.org

The site is clunky and unprofessional looking. Needs to be toned down so the urgency is conveyed, but not via a burning planet image.

Target Market(s)

Non-profit climate adaptation group targeting local government land management agencies, special districts and private landholders of natural resource properties.

Industry/Entity Type

Environment

Coding

Coded - Design and coding required

Number of Pages Required

Font styles to use
Serif
Sans Serif

Requirements
Must have
• Include current logos, aspects if content on current site www.cedarlinecoalition.org
• A regional Pacific Northwest Focus (US & Canada). Content speaking to urgency but respectful of cultural diversity and norms. Sustainability themes. Emphasis on action and implementation.
Nice to have
• link to like minded projects. Appear to future generations. Diversity in thematic areas ecological resiliency, energy, food security and infrastructure.

```html
<!DOCTYPE html>
<html lang="en">
<head>
<meta charset="utf-8">
<title>Cedarline Coalition — Climate Adaptation</title>
<link href="https://fonts.googleapis.com/css2?family=Poppins:wght@400;500;600&display=swap" rel="stylesheet">
<style>
:root{
  --blue:#1a8ccb;
  --green:#a5cf4c;
  --green-text:#8cc63f;
  --ink:#333;
  --muted:#777;
  --card:#f5f5f5;
  --card-line:#c9c9c9;
  --pale:#f5f5f5;
  --white:#fff;
}
*{box-sizing:border-box;margin:0;padding:0}
html,body{width:1200px;height:3078px;overflow:hidden}
body{font-family:"Poppins",sans-serif;color:var(--ink);position:relative;background:var(--white)}
section,header,footer,.topbar{position:absolute;left:0;width:1200px}
.wrap{position:absolute;left:147px;width:912px}

/* top bar */
.topbar{top:0;height:40px;background:var(--blue);color:var(--white);font-size:11px}
.topbar .contact{position:absolute;left:147px;top:12px;display:flex;gap:22px;align-items:center}
.topbar .contact span{display:flex;align-items:center;gap:8px}
.topbar .social{position:absolute;right:141px;top:12px;display:flex;gap:12px}
.topbar .social i{display:block;width:16px;height:16px;border-radius:50%;background:rgba(255,255,255,.85)}

/* header */
.site-header{top:40px;height:82px;background:var(--white)}
.brand{position:absolute;left:147px;top:26px;display:flex;align-items:center;gap:8px;font-size:17px;font-weight:600;color:var(--blue)}
.brand .dot{width:22px;height:22px;border-radius:50%;background:var(--green)}
.nav{position:absolute;left:584px;top:38px;display:flex;gap:24px;font-size:10px;font-weight:500;color:#555}
.nav a{color:inherit;text-decoration:none}
.nav .active{color:var(--green-text)}
.search{position:absolute;left:1044px;top:36px}

/* hero */
.hero{top:122px;height:512px;background:linear-gradient(180deg,#2b2226 0%,#5a2e24 30%,#a3522a 52%,#6a3a2a 66%,#2a2022 100%);text-align:center;color:var(--white)}
.hero .kicker{position:absolute;top:134px;width:100%;font-size:25px;font-weight:500}
.hero h1{position:absolute;top:166px;width:100%;font-size:39px;font-weight:600;color:var(--green)}
.hero p{position:absolute;top:222px;left:230px;width:740px;font-size:15.5px;line-height:20px}
.hero .btn{position:absolute;top:326px;left:510px;width:180px;height:46px;background:var(--green);color:var(--white);font-size:19px;font-weight:600;line-height:46px}

/* featured */
.featured{top:634px;height:474px;text-align:center}
.section-title{font-size:26px;font-weight:600;color:var(--blue)}
.featured .section-title{position:absolute;top:76px;width:100%}
.featured .lead{position:absolute;top:120px;left:260px;width:680px;font-size:11.5px;line-height:19px;color:var(--muted)}
.cards{position:absolute;top:185px;left:147px;display:flex;gap:18px}
.card{width:215px;height:207px;background:var(--card);border:2px solid var(--card-line);padding:22px 10px 0}
.card .ico{width:66px;height:66px;border-radius:50%;background:var(--green);margin:0 auto 12px;display:flex;align-items:center;justify-content:center}
.card h3{font-size:15px;font-weight:500;color:var(--green-text);margin-bottom:4px}
.card p{font-size:10px;line-height:13.5px;color:#666;height:41px;overflow:hidden}
.card a{display:block;margin-top:6px;font-size:10px;color:var(--blue);text-decoration:none}

/* doing */
.doing{top:1108px;height:395px;background:var(--blue);color:var(--white)}
.doing h2{position:absolute;left:147px;top:106px;font-size:24px;font-weight:600}
.doing .copy{position:absolute;left:147px;top:157px;width:449px;font-size:11.3px;line-height:16.3px;text-align:justify}
.doing .copy p+p{margin-top:16px}
.photo{border:3px solid var(--white)}
.doing .photo{position:absolute;left:673px;top:70px;width:386px;height:256px}
.tree-photo{background:radial-gradient(ellipse at 50% 45%,#3f8a2a 0%,#2d6a1e 22%,#8a7a4a 48%,#5a5236 75%,#3a3a24 100%)}

/* stats */
.stats{top:1503px;height:322px}
.stat{position:absolute;top:84px;width:156px;height:156px;background:var(--green);color:var(--white);text-align:center}
.stat svg{margin-top:28px}
.stat strong{display:block;font-size:31px;font-weight:600;line-height:36px;margin-top:4px}
.stat span{display:block;font-size:12.5px;line-height:13px;margin-top:4px;padding:0 30px}

/* recent */
.recent{top:1825px;height:470px;background:var(--pale)}
.recent .section-title{position:absolute;top:80px;width:100%;text-align:center}
.gallery{position:absolute;top:132px;left:0;display:flex}
.gallery div{width:400px;height:255px}
.g-road{background:linear-gradient(180deg,#6f9a2a 0%,#8dbb3a 45%,#5c7a24 75%,#aab45a 100%)}
.g-bridge{background:linear-gradient(180deg,#2e5a1e 0%,#3f7a28 45%,#2a4a1c 70%,#1e3316 100%)}
.g-arch{background:linear-gradient(180deg,#cfe0c4 0%,#5f8a3a 30%,#556a4a 60%,#8a9a80 100%)}

/* save */
.save{top:2295px;height:397px;background:var(--green)}
.save .photo{position:absolute;left:149px;top:70px;width:386px;height:257px}
.save h2{position:absolute;left:564px;top:86px;font-size:26px;font-weight:600;color:var(--white)}
.bars{position:absolute;left:564px;top:137px}
.bar{position:relative;width:435px;height:31px;background:var(--white);border:2px solid var(--white);margin-bottom:12px}
.bar .fill{height:100%;background:var(--blue);color:var(--white);font-size:11px;font-weight:600;line-height:27px;padding-left:15px}
.bar em{position:absolute;left:447px;top:5px;font-style:normal;font-size:13px;font-weight:600;color:var(--white)}

/* footer */
.site-footer{top:2692px;height:339px;text-align:center}
.footer-brand{position:absolute;top:84px;width:100%;display:flex;justify-content:center;align-items:center;gap:10px;font-size:26px;font-weight:600;color:var(--blue)}
.footer-brand .dot{width:30px;height:30px;border-radius:50%;background:var(--green)}
.links{position:absolute;width:100%;font-size:11.5px;color:#666}
.links span{margin:0 13px}
.links.primary{top:170px}
.links.secondary{top:210px}
.rule{position:absolute;left:392px;top:200px;width:416px;border-top:1px solid #ddd}
.foot-social{position:absolute;top:244px;width:100%;display:flex;justify-content:center;gap:9px}
.foot-social i{width:26px;height:26px;background:var(--blue)}
.copyright{position:absolute;top:290px;width:100%;font-size:11px;color:#666}
.bottom-bar{position:absolute;left:0;top:3031px;width:1200px;height:47px;background:var(--green)}
.to-top{position:absolute;left:581px;top:3012px;width:38px;height:38px;background:var(--white);transform:rotate(45deg);border:1px solid #e2e2e2}
.to-top svg{transform:rotate(-45deg);margin:9px}
</style>
</head>
<body>

<div class="topbar">
  <div class="contact">
    <span><svg width="14" height="14" viewBox="0 0 24 24"><path fill="#fff" d="M6.6 10.8a15 15 0 0 0 6.6 6.6l2.2-2.2c.3-.3.7-.4 1-.2 1.1.4 2.3.6 3.6.6.6 0 1 .4 1 1V20c0 .6-.4 1-1 1A17 17 0 0 1 3 4c0-.6.4-1 1-1h3.5c.6 0 1 .4 1 1 0 1.3.2 2.5.6 3.6.1.3 0 .7-.2 1z"/></svg>360-555-0182</span>
    <span><svg width="15" height="11" viewBox="0 0 15 11"><rect x=".5" y=".5" width="14" height="10" fill="none" stroke="#fff"/><path d="M.5.5l7 6 7-6" fill="none" stroke="#fff"/></svg>info@cedarlinecoalition.org</span>
  </div>
  <div class="social"><i></i><i></i><i></i><i></i><i></i></div>
</div>

<header class="site-header">
  <div class="brand"><span class="dot"></span>Cedarline Coalition</div>
  <nav class="nav">
    <a class="active">HOME</a><a>ABOUT US</a><a>FEATURED PROJECTS</a><a>RECENT WORK</a><a>CONTACT US</a>
  </nav>
  <svg class="search" width="16" height="16" viewBox="0 0 16 16"><circle cx="6.5" cy="6.5" r="5.5" fill="none" stroke="#777" stroke-width="1.5"/><path d="M10.5 10.5L15 15" stroke="#777" stroke-width="1.5"/></svg>
</header>

<section class="hero" role="img" aria-label="Sunset over tidal flats with tree branches silhouetted">
  <div class="kicker">CLIMATE ADAPTATION</div>
  <h1>Implementing Climate Strategies</h1>
  <p>Dedicated to taking action the Cedarline Coalition was created to help bring adaption strategies to life. Working with local communities we are committed to implementing strategies that will sustain communities throughout the Pacific Northwest for generations to come.</p>
  <div class="btn">Contact Us</div>
</section>

<section class="featured">
  <h2 class="section-title">Featured Projects</h2>
  <p class="lead">We are hyper focused on IMPLEMENTATION. We are eager to get about the business of preparing communities in the Pacific Northwest for fundamental change brought on by shifts in our climate and ecology.</p>
  <div class="cards">
    <div class="card">
      <div class="ico"><svg width="30" height="30" viewBox="0 0 30 30" fill="none" stroke="#fff" stroke-width="1.6"><path d="M10 3l7 11H3z"/><circle cx="7" cy="22" r="5"/><rect x="15" y="17" width="10" height="10"/></svg></div>
      <h3>Adaptation Plans</h3>
      <p>Communities throughout the region have adopted plans to to address our changing climate.</p>
      <a>Read More</a>
    </div>
    <div class="card">
      <div class="ico"><svg width="22" height="30" viewBox="0 0 22 30" fill="none" stroke="#fff" stroke-width="1.6"><path d="M11 2C7 10 3 14 3 19a8 8 0 0 0 16 0c0-5-4-9-8-17z"/></svg></div>
      <h3>On The Ground</h3>
      <p>The Coalition is familiar and growing throughout the region. Presently our work has us on the ground in</p>
      <a>Read More</a>
    </div>
    <div class="card">
      <div class="ico"><svg width="30" height="30" viewBox="0 0 30 30" fill="none" stroke="#fff" stroke-width="1.6"><circle cx="15" cy="16" r="10"/><path d="M8 12c3 0 4 3 7 2s2 5 5 5M15 6c2-3 6-3 7 0"/></svg></div>
      <h3>Ecological Resilience</h3>
      <p>To endure change Communities need to keep their watersheds functioning. Our network or professionals have</p>
      <a>Read More</a>
    </div>
    <div class="card">
      <div class="ico"><svg width="24" height="32" viewBox="0 0 24 32" fill="none" stroke="#fff" stroke-width="1.6"><rect x="4" y="3" width="16" height="26" rx="2"/><path d="M13 9l-4 8h5l-3 7"/></svg></div>
      <h3>Energy and Food</h3>
      <p>Security of community food and energy have, and always will be, an essential component of how</p>
      <a>Read More</a>
    </div>
  </div>
</section>

<section class="doing">
  <h2>What We Are Doing?</h2>
  <div class="copy">
    <p>Lorem Ipsum is simply dummy text of the printing and typesetting industry. Lorem Ipsum has been the industry's standard dummy text ever since the 1500s, when an unknown printer took a galley of type and scrambled it to make a type specimen book. It has survived not only five centuries, but also the leap into electronic typesetting, remaining essentially unchanged.</p>
    <p>Lorem Ipsum is simply dummy text of the printing and typesetting industry. Lorem Ipsum has been the industry's standard dummy.</p>
  </div>
  <div class="photo tree-photo" role="img" aria-label="Small tree growing inside a broken glass sphere"></div>
</section>

<section class="stats">
  <div class="stat" style="left:173px">
    <svg width="28" height="28" viewBox="0 0 28 28" fill="none" stroke="#fff" stroke-width="2"><circle cx="14" cy="14" r="11" stroke-dasharray="3 2"/><circle cx="14" cy="14" r="6"/><path d="M11 14l2 2 4-4"/></svg>
    <strong>250+</strong><span>Projects Completed</span>
  </div>
  <div class="stat" style="left:406px">
    <svg width="36" height="36" viewBox="0 0 36 36" fill="none" stroke="#fff" stroke-width="2"><path d="M6 14l8-8 6 6M30 22l-8 8-6-6M10 24l4 4M26 12l-4-4M12 18l6 6 6-6-6-6z"/></svg>
    <strong>300+</strong><span>Donations</span>
  </div>
  <div class="stat" style="left:638px">
    <svg width="28" height="28" viewBox="0 0 28 28" fill="#fff"><path d="M7 3h14v7a7 7 0 0 1-14 0zM3 5h4v3a3 3 0 0 1-4-3zM25 5h-4v3a3 3 0 0 0 4-3zM12 17h4v5h-4zM8 23h12v3H8z"/></svg>
    <strong>17+</strong><span>Communities Engaged</span>
  </div>
  <div class="stat" style="left:871px">
    <svg width="32" height="28" viewBox="0 0 32 28" fill="#fff"><circle cx="16" cy="8" r="5"/><circle cx="7" cy="10" r="3.5"/><circle cx="25" cy="10" r="3.5"/><path d="M7 24c0-6 4-9 9-9s9 3 9 9zM1 22c0-4 2-7 6-7 1 0 2 .2 3 .6-2 2-3 4-3 6.4zM31 22c0-4-2-7-6-7-1 0-2 .2-3 .6 2 2 3 4 3 6.4z"/></svg>
    <strong>70+</strong><span>Volunteers</span>
  </div>
</section>

<section class="recent">
  <h2 class="section-title">Recent Work</h2>
  <div class="gallery">
    <div class="g-road" role="img" aria-label="Country road lined with green trees"></div>
    <div class="g-bridge" role="img" aria-label="Wooden footbridge reflected in a forest pond"></div>
    <div class="g-arch" role="img" aria-label="Stone arch bridge reflected in a lake"></div>
  </div>
</section>

<section class="save">
  <div class="photo tree-photo" role="img" aria-label="Small tree growing inside a broken glass sphere"></div>
  <h2>Think Green ! Save Money</h2>
  <div class="bars">
    <div class="bar"><div class="fill" style="width:86%">Clean Water</div><em>90%</em></div>
    <div class="bar"><div class="fill" style="width:57%">Forest Rescue</div><em>56%</em></div>
    <div class="bar"><div class="fill" style="width:64%">Agriculture</div><em>67%</em></div>
    <div class="bar"><div class="fill" style="width:73%">Alternative Energy</div><em>75%</em></div>
  </div>
</section>

<footer class="site-footer">
  <div class="footer-brand"><span class="dot"></span>Cedarline Coalition</div>
  <div class="links primary"><span>About Us</span>|<span>Causes</span>|<span>Testimonial</span>|<span>Events</span>|<span>Contact Us</span></div>
  <div class="rule"></div>
  <div class="links secondary"><span>Terms &amp; Conditions</span>|<span>Privacy Policy</span>|<span>Accessibility</span></div>
  <div class="foot-social"><i></i><i></i><i></i><i></i><i></i></div>
  <div class="copyright">Copyright © 2020 All Reserved.</div>
</footer>

<div class="bottom-bar"></div>
<div class="to-top"><svg width="18" height="18" viewBox="0 0 18 18" fill="none" stroke="#a5cf4c" stroke-width="2"><path d="M9 16V3M3 9l6-6 6 6"/></svg></div>

</body>
</html>
```